Marrowfell Website Concept

We would like a one page website. Please refer to the attached files for more information.

Please reference file attachment version 1.1.

```html
<!DOCTYPE html>
<html lang="en">
<head>
<meta charset="utf-8">
<title>Marrowfell Security</title>
<link rel="stylesheet" href="https://fonts.googleapis.com/css2?family=Oswald:wght@400;500&family=Arimo:wght@400;700&display=swap">
<style>
:root{
  --ink:#1f2d44;
  --navy:#1c3550;
  --slate:#5d7186;
  --field:#5f738a;
  --panel:#d9dbdd;
  --grey-line:#8b9096;
  --text:#4a4f56;
  --link-blue:#3f6fa1;
  --footer:#121417;
  --footer-text:#c9ccd0;
  --bar:#dcdde0;
  --white:#ffffff;
  --btn:#1d3a5c;
}
*{box-sizing:border-box;margin:0;padding:0}
html,body{width:1200px;height:2687px;overflow:hidden;background:var(--white)}
body{position:relative;font-family:"Arimo",Arial,sans-serif;color:var(--text)}
.abs{position:absolute}
.heading{font-family:"Oswald","Arial Narrow",sans-serif;font-weight:400;color:var(--ink);white-space:nowrap}

/* header */
.site-header{left:0;top:0;width:1200px;height:134px;background:linear-gradient(#f4f4f4,#e6e7e8)}
.brand{left:44px;top:30px;display:flex;align-items:center;gap:14px}
.brand-dot{width:50px;height:50px;border-radius:50%;background:var(--navy)}
.brand-name{font-family:"Oswald",sans-serif;font-weight:500;font-size:42px;line-height:1;color:var(--ink);letter-spacing:1px}
.social{top:18px;width:42px;height:42px;border-radius:50%;background:#9a9da1}
.nav-link{top:88px;font-size:17px;color:var(--link-blue);white-space:nowrap}

.hero{left:0;top:134px;width:1200px;height:493px;background:linear-gradient(120deg,#cfd3d6 0%,#eef0f1 40%,#b7bdc0 70%,#6f7a6e 100%)}

/* section titles */
.section-title{font-size:36px;line-height:50px;text-align:center;width:1200px;left:0}
.divider{height:2px;background:var(--grey-line)}
.divider::before,.divider::after{content:"";position:absolute;top:-5px;width:12px;height:12px;border-radius:50%;background:var(--grey-line)}
.divider::before{left:-6px}.divider::after{right:-6px}

/* cards */
.card{top:749px;height:349px;background:linear-gradient(#8a8f93,#cfd2d4 55%,#f3f3f3 75%)}
.card-title{position:absolute;left:0;top:252px;width:100%;text-align:center;font-family:"Oswald",sans-serif;font-size:23px;line-height:32px;color:var(--ink);white-space:nowrap}
.read-more{position:absolute;left:50%;top:297px;transform:translateX(-50%);width:100px;height:28px;border:2px solid var(--ink);border-radius:14px;background:var(--white);font-size:12px;color:var(--ink);text-align:center;line-height:24px}
.about{left:120px;top:1116px;width:960px;font-size:15.5px;line-height:24.5px;text-align:center;color:var(--text)}
.about b{color:var(--link-blue);font-weight:400}

/* services */
.services{left:0;top:1272px;width:1200px;height:265px;background:linear-gradient(90deg,#101318,#27323e 50%,#101318)}
.services .section-title{color:var(--white);top:17px}
.service-icon{top:110px;width:92px;height:92px;border-radius:50%;background:#6b7480;border:3px solid #9aa2ab;display:flex;align-items:center;justify-content:center}
.service-name{top:118px;font-size:17px;color:var(--white);white-space:nowrap}
.service-copy{top:146px;width:160px;font-size:14.5px;line-height:20px;color:#9aa7b4}

/* testimonials */
.test-wrap{left:101px;top:1660px;width:642px;height:609px;background:var(--panel)}
.test-card{left:119px;top:1681px;width:606px;height:567px;background:var(--slate)}
.portrait{left:140px;top:1713px;width:275px;height:248px;border:4px solid #e5e7ea;background:linear-gradient(#e9e6df,#c9a68a 60%,#8a6a56)}
.quote-mark{font-family:"Oswald",sans-serif;font-size:84px;color:var(--white);line-height:1}
.test-text{font-size:15.5px;line-height:24px;color:var(--white)}

/* contact form */
.form-wrap{left:794px;top:1660px;width:304px;height:609px;background:var(--panel)}
.field{left:818px;width:260px;height:39px;background:var(--field);color:var(--white);font-size:14px;padding:11px 12px}
.send{left:818px;top:2212px;width:128px;height:38px;background:var(--btn);color:var(--white);font-size:15px;text-align:center;line-height:38px}

/* footer */
.site-footer{left:0;top:2296px;width:1200px;height:331px;background:radial-gradient(ellipse at 50% 40%,#2c333c,var(--footer) 70%)}
.foot-head{font-family:"Oswald",sans-serif;font-size:22px;line-height:30px;color:var(--white);top:2331px;white-space:nowrap}
.foot-rule{top:2366px;height:2px;background:#6a7078}
.foot-links{top:2377px;list-style:none;font-size:14px;line-height:28.5px;color:var(--footer-text)}
.news{left:797px;top:2388px;width:281px;height:200px;background:#2a3d55}
.news p{position:absolute;left:18px;top:16px;width:250px;font-size:13px;line-height:19px;color:var(--footer-text)}
.news .email{position:absolute;left:27px;top:74px;width:227px;height:34px;background:var(--white);font-size:13px;color:#999;padding:9px 14px}
.news .submit{position:absolute;left:15px;top:155px;width:254px;height:42px;background:#2f5d8c;border:2px solid #c9d3de;color:var(--white);font-size:13px;font-weight:700;text-align:center;line-height:38px}
.bottom-bar{left:0;top:2627px;width:1200px;height:60px;background:var(--bar);font-size:13px;color:#55595f}
.bottom-bar span{position:absolute;top:22px;white-space:nowrap}
</style>
</head>
<body>

<header class="abs site-header">
  <div class="abs brand"><span class="brand-dot"></span><span class="brand-name">Marrowfell</span></div>
  <span class="abs social" style="left:952px"></span>
  <span class="abs social" style="left:1006px"></span>
  <span class="abs social" style="left:1060px"></span>
  <span class="abs nav-link" style="left:639px">Company Description</span>
  <span class="abs nav-link" style="left:840px">Service Offerings</span>
  <span class="abs nav-link" style="left:1018px">Contact Us</span>
</header>

<div class="abs hero" role="img" aria-label="Photo of a hand writing with a pen beside a calculator and coins on financial papers"></div>

<h2 class="abs heading section-title" style="top:655px">Company Description</h2>
<div class="abs divider" style="left:116px;top:718px;width:968px"></div>

<div class="abs card" style="left:101px;width:320px" role="img" aria-label="Photo of a modern conference room">
  <div class="card-title">MARROWFELL SECURITY</div><div class="read-more">Read More</div>
</div>
<div class="abs card" style="left:442px;width:319px" role="img" aria-label="Photo of smiling business professionals">
  <div class="card-title">FINANCIAL SERVICES</div><div class="read-more">Read More</div>
</div>
<div class="abs card" style="left:782px;width:316px" role="img" aria-label="Photo of a business team">
  <div class="card-title">OUR SERVICES</div><div class="read-more">Read More</div>
</div>

<p class="abs about"><b>Marrowfell Security</b>, LLC is a United States-based tier one security firm specializing in the protection of financial services professionals, executives and their families. We manage engagements resulting from general and specific threats throughout the United States and abroad on behalf of our domestic clients. We deliver our services exclusively through associates and contractors with United States special operations, secret service, CIA, or equivalent experience and training. We are one of only a handful of domestic security firms that offers scalable, tier one security services in every market in the United States.</p>

<section class="abs services">
  <h2 class="abs heading section-title">Service Offerings</h2>
  <div class="abs divider" style="left:116px;top:80px;width:968px;background:#7e8893"></div>

  <div class="abs service-icon" style="left:99px"><svg width="60" height="60" viewBox="12 12 60 60"><rect x="24" y="26" width="36" height="26" fill="none" stroke="#fff" stroke-width="3"/><polyline points="29,46 37,38 44,43 54,32" fill="none" stroke="#fff" stroke-width="3"/><line x1="42" y1="52" x2="42" y2="60" stroke="#fff" stroke-width="3"/><line x1="33" y1="60" x2="51" y2="60" stroke="#fff" stroke-width="3"/></svg></div>
  <div class="abs service-name" style="left:221px">Threat Assessment</div>
  <div class="abs service-copy" style="left:221px">Donec et libero quis erat commodo sapien. Mae sit a, eleifend leo</div>

  <div class="abs service-icon" style="left:441px"><svg width="60" height="60" viewBox="12 12 60 60"><circle cx="42" cy="46" r="16" fill="none" stroke="#fff" stroke-width="4"/><line x1="42" y1="46" x2="50" y2="38" stroke="#fff" stroke-width="4"/><rect x="37" y="22" width="10" height="6" fill="#fff"/></svg></div>
  <div class="abs service-name" style="left:564px">Threat Avoidance Plan</div>
  <div class="abs service-copy" style="left:564px">Donec et libero quis erat commodo sapien. Mae sit a, eleifend leo</div>

  <div class="abs service-icon" style="left:790px"><svg width="60" height="60" viewBox="12 12 60 60"><circle cx="42" cy="34" r="7" fill="#fff"/><path d="M30 56c0-9 5-13 12-13s12 4 12 13z" fill="#fff"/><circle cx="26" cy="38" r="5" fill="#fff"/><path d="M17 54c0-7 4-10 9-10 2 0 3 0 4 1-2 2-3 5-3 9z" fill="#fff"/><circle cx="58" cy="38" r="5" fill="#fff"/><path d="M67 54c0-7-4-10-9-10-2 0-3 0-4 1 2 2 3 5 3 9z" fill="#fff"/></svg></div>
  <div class="abs service-name" style="left:911px">Elite Executive Protection</div>
  <div class="abs service-copy" style="left:911px">Donec et libero quis erat commodo sapien. Mae sit a, eleifend leo</div>
</section>

<h2 class="abs heading" style="left:99px;top:1563px;font-size:36px;line-height:50px">Testimonials</h2>
<div class="abs divider" style="left:107px;top:1627px;width:630px"></div>
<h2 class="abs heading" style="left:794px;top:1563px;font-size:36px;line-height:50px">Contact Us Form</h2>
<div class="abs divider" style="left:800px;top:1627px;width:292px"></div>

<div class="abs test-wrap"></div>
<div class="abs test-card"></div>
<div class="abs portrait" role="img" aria-label="Portrait photo of a smiling client"></div>
<div class="abs quote-mark" style="left:430px;top:1712px">&ldquo;</div>
<p class="abs test-text" style="left:478px;top:1742px;width:245px">Lorem ipsum dolor sit amet, consectetuer adipiscing elit, sed diam nonummy nibh euismod tincidunt ut laoreet dolore magna aliquam erat volutpat. Ut wisi enim ad minim veniam, quis nostrud exerci tation ullamcorper suscipit lobortis nisl ut aliquip ex ea commodo consequat.</p>
<p class="abs test-text" style="left:140px;top:1979px;width:570px">Lorem ipsum dolor sit amet, consectetuer adipiscing elit, sed diam nonummy nibh euismod tincidunt ut laoreet dolore magna aliquam erat volutpat. Ut wisi enim ad minim veniam, quis nostrud exerci tation ullamcorper suscipit lobortis nisl ut aliquip ex ea commodo consequat. Duis autem vel eum iriure dolor in hendrerit in vulputate velit esse molestie consequat, vel illum dolore eu feugiat nulla facilisis at vero eros et accumsan et iusto odio dignissim qui blandit praesent luptatum zzril delenit augue duis dolore te feugait nulla facilisi.</p>
<div class="abs quote-mark" style="left:665px;top:2140px">&rdquo;</div>
<div class="abs test-text" style="left:140px;top:2206px">- Lorem Ipsum</div>
<div class="abs test-text" style="left:632px;top:2206px">Read More</div>

<div class="abs form-wrap"></div>
<div class="abs field" style="top:1683px">First Name</div>
<div class="abs field" style="top:1730px">Last Name</div>
<div class="abs field" style="top:1778px">Home Phone</div>
<div class="abs field" style="top:1825px">Work Phone</div>
<div class="abs field" style="top:1873px">Cell Phone</div>
<div class="abs field" style="top:1920px">Email Address</div>
<div class="abs field" style="top:1968px">City</div>
<div class="abs field" style="top:2015px">State</div>
<div class="abs field" style="top:2063px">Zip</div>
<div class="abs field" style="top:2110px;height:86px">Message</div>
<div class="abs send">Send</div>

<footer class="abs site-footer" role="img" aria-label="Dark background photo of a person in a suit"></footer>
<div class="abs foot-head" style="left:119px">INFORMATIONS</div>
<div class="abs foot-rule" style="left:119px;width:272px"></div>
<ul class="abs foot-links" style="left:119px">
  <li>About Us</li><li>Customer Service</li><li>Template Settings</li><li>Site Map</li><li>Contact Us</li>
</ul>
<div class="abs foot-head" style="left:481px">COMPANY</div>
<div class="abs foot-rule" style="left:481px;width:272px"></div>
<ul class="abs foot-links" style="left:481px">
  <li>Our business</li><li>Timbers</li><li>Enquiries</li><li>Environment</li><li>Terms</li>
</ul>
<div class="abs foot-head" style="left:797px">NEWS LETTER</div>
<div class="abs foot-rule" style="left:797px;width:262px"></div>
<div class="abs news">
  <p>Quisque volutpat mattis eros. Nullamma malesuada erat ut turpes.</p>
  <div class="email">Email</div>
  <div class="submit">SUBMIT</div>
</div>

<div class="abs bottom-bar">
  <span style="left:99px">Copyright &copy; 2014 Creation All Rights Reserved. Designed &amp; Developed By Northgate Studio</span>
  <span style="left:727px">Company Description &nbsp;/&nbsp; Service Offerings &nbsp;/&nbsp; Contact Us</span>
</div>
</body>
</html>
```